New professional looking flyer for company

I need our flyer updated my flyer is the Lvb flyer Have attached current flyer so you know what services need to be listed. Want it to be in mainly dark colours like black and dark grey with pops of light grey, silver or white. i have added several photos for you to choose which ones work best with your design would like The photos to be in colour for the flyer. But can have a mix of greyscale if that works for your design j have attached another companies flyers as design ideas to show what I am looking for

Target Market(s)

new clients

Industry/Entity Type

transport and earthmoving

Colors

Designer to choose colors to be used in the design.

Requirements
Nice to have
• Look professional
Should not have
• No orange or red or green

```html
<!DOCTYPE html>
<html lang="en">
<head>
<meta charset="utf-8">
<title>Lvb Pty Ltd flyer</title>
<link rel="stylesheet" href="https://fonts.googleapis.com/css2?family=Montserrat:wght@400;500;700;800&display=swap">
<style>
  :root {
    --page-bg: #dcdbdc;
    --black: #000000;
    --panel-grey: #58585a;
    --soft-grey: #b3b3b3;
    --white: #ffffff;
    --ink: #111111;
    --body-text: #444444;
    --tick: #58585a;
    --highlight: #c9c9c9;
    --logo-silver: #d6d6d6;
  }
  html, body {
    margin: 0;
    padding: 0;
    width: 1200px;
    height: 1200px;
    overflow: hidden;
    background: var(--page-bg);
    font-family: "Montserrat", sans-serif;
  }
  .flyer {
    position: absolute;
    left: 186px;
    top: 20px;
    width: 1210px;
    height: 1697px;
    background: var(--white);
    overflow: hidden;
    transform: scale(0.6836);
    transform-origin: top left;
  }
  .hero-band {
    position: absolute;
    left: 0; top: 0;
    width: 1210px; height: 670px;
    background: var(--black);
  }
  .brand-panel {
    position: absolute;
    left: 568px; top: 0;
    width: 592px; height: 965px;
    background: var(--panel-grey);
    border-radius: 0 0 296px 296px;
  }
  .photo {
    position: absolute;
  }
  .photo-lowboy {
    left: 75px; top: 60px;
    width: 1065px; height: 580px;
    background: linear-gradient(135deg, rgba(90,90,90,0.5), rgba(200,200,200,0.5));
    border-radius: 6px;
  }
  .hero-copy {
    position: absolute;
    left: 120px; top: 385px;
    color: var(--white);
    z-index: 2;
  }
  .hero-title {
    margin: 0;
    font-size: 47px;
    font-weight: 700;
    letter-spacing: 0.3px;
  }
  .hero-lead {
    margin: 6px 0 0 8px;
    font-size: 27px;
    font-weight: 400;
    line-height: 33px;
    width: 290px;
  }
  .hero-note {
    margin: 28px 0 0 8px;
    font-size: 23px;
    line-height: 28px;
    color: var(--highlight);
    width: 320px;
  }
  .brand-name {
    position: absolute;
    left: 568px; top: 760px;
    width: 592px;
    text-align: center;
    font-size: 70px;
    font-weight: 800;
    color: var(--logo-silver);
    margin: 0;
  }
  .services {
    position: absolute;
    margin: 0;
    padding: 0;
    list-style: none;
    color: var(--body-text);
    font-size: 20px;
    font-weight: 500;
  }
  .services li {
    position: relative;
    padding-left: 35px;
    line-height: 24px;
    margin-bottom: 12px;
  }
  .services svg {
    position: absolute;
    left: 0; top: 3px;
    width: 20px; height: 18px;
    color: var(--tick);
  }
  .services-heading {
    position: absolute;
    left: 130px; top: 700px;
    margin: 0;
    font-size: 24px;
    font-weight: 700;
    color: var(--ink);
  }
  .services-primary { left: 128px; top: 742px; }
  .services-secondary { left: 757px; top: 1018px; width: 400px; }
  .tanker-band {
    position: absolute;
    left: 0; top: 937px;
    width: 700px; height: 445px;
    background: var(--soft-grey);
    border-radius: 0 222px 222px 0;
  }
  .photo-tanker {
    left: 25px; top: 1010px;
    width: 625px; height: 250px;
    background: linear-gradient(90deg, rgba(230,230,230,0.8), rgba(40,40,40,0.85));
    border-radius: 6px;
  }
  .photo-buildings {
    left: 480px; top: 1282px;
    width: 715px; height: 370px;
    background: linear-gradient(90deg, #2a2a2a, #8f8f8f 65%, #d0d0d0);
    border-radius: 6px;
  }
  .contact {
    position: absolute;
    left: 60px; top: 1432px;
    color: var(--ink);
    z-index: 2;
  }
  .contact-call {
    margin: 0;
    font-size: 68px;
    font-weight: 800;
    line-height: 78px;
  }
  .contact-phone {
    margin: 8px 0 0 8px;
    font-size: 34px;
    font-weight: 800;
  }
  .contact-address {
    margin: 10px 0 0 8px;
    font-size: 22px;
    color: var(--body-text);
  }
  .contact-email {
    margin: 6px 0 0 8px;
    font-size: 22px;
    font-weight: 700;
    color: var(--body-text);
  }
</style>
</head>
<body>
<main class="flyer">
  <div class="hero-band"></div>
  <div class="brand-panel"></div>
  <div class="photo photo-lowboy" role="img" aria-label="Prime mover hauling a grader on a low loader trailer, oversize load"></div>

  <section class="hero-copy">
    <h1 class="hero-title">Call Us Today</h1>
    <p class="hero-lead">for a personalized quote to suit your needs.</p>
    <p class="hero-note">We offer a large range of services not listed!!!</p>
  </section>

  <p class="brand-name">Lvb Pty Ltd</p>

  <h2 class="services-heading">Ours Services</h2>
  <ul class="services services-primary">
    <li><svg viewBox="0 0 20 18"><path d="M1 10 L7 16 L19 2" fill="none" stroke="currentColor" stroke-width="3.5"/></svg>Over Size Loads / Hot Shot Loads</li>
    <li><svg viewBox="0 0 20 18"><path d="M1 10 L7 16 L19 2" fill="none" stroke="currentColor" stroke-width="3.5"/></svg>Heavy Vehicle Recovery Services</li>
    <li><svg viewBox="0 0 20 18"><path d="M1 10 L7 16 L19 2" fill="none" stroke="currentColor" stroke-width="3.5"/></svg>Portable Water Deliveries</li>
    <li><svg viewBox="0 0 20 18"><path d="M1 10 L7 16 L19 2" fill="none" stroke="currentColor" stroke-width="3.5"/></svg>Road Building /Maintenance</li>
    <li><svg viewBox="0 0 20 18"><path d="M1 10 L7 16 L19 2" fill="none" stroke="currentColor" stroke-width="3.5"/></svg>Earthworks</li>
  </ul>

  <div class="tanker-band"></div>
  <div class="photo photo-tanker" role="img" aria-label="Road train prime mover pulling three water tanker trailers"></div>

  <ul class="services services-secondary">
    <li><svg viewBox="0 0 20 18"><path d="M1 10 L7 16 L19 2" fill="none" stroke="currentColor" stroke-width="3.5"/></svg>Sand &amp; Metal Suply &amp; Cartage</li>
    <li><svg viewBox="0 0 20 18"><path d="M1 10 L7 16 L19 2" fill="none" stroke="currentColor" stroke-width="3.5"/></svg>Road Train Tippers</li>
    <li><svg viewBox="0 0 20 18"><path d="M1 10 L7 16 L19 2" fill="none" stroke="currentColor" stroke-width="3.5"/></svg>Road Train Tankers</li>
    <li><svg viewBox="0 0 20 18"><path d="M1 10 L7 16 L19 2" fill="none" stroke="currentColor" stroke-width="3.5"/></svg>Road Train Flat Tops</li>
    <li><svg viewBox="0 0 20 18"><path d="M1 10 L7 16 L19 2" fill="none" stroke="currentColor" stroke-width="3.5"/></svg>Drop Deck Trailers</li>
    <li><svg viewBox="0 0 20 18"><path d="M1 10 L7 16 L19 2" fill="none" stroke="currentColor" stroke-width="3.5"/></svg>Mine Sites Accredited Equipment &amp; Operators</li>
  </ul>

  <div class="photo photo-buildings" role="img" aria-label="Road train prime mover hauling transportable site buildings, oversize load"></div>

  <section class="contact">
    <p class="contact-call">CALL NOW</p>
    <p class="contact-phone">+00 111 222 333</p>
    <p class="contact-address">1234 Your Address, Your City</p>
    <p class="contact-email">info@lvb.com.au</p>
  </section>
</main>
</body>
</html>
```